Business Card Design Project

My business sells promotional merchandise to large blue chip companies. Gear like polo shirts, drink bottles, pens, basically anything that you can put a company logo onto.

I need the following elements included:
Logo as attached
Peter Hollingdale Managing Director
27 Corbel Street Tarrin Cove 4178
mobile 0438 514203
email kestrelpath@kestrelpathtrading.com.au

Promotional Merchandise with a difference

Target Market(s)

Mature age Marketing Managers

Industry/Entity Type

Business

```html
<!DOCTYPE html>
<html lang="en">
<head>
<meta charset="utf-8">
<title>Kestrel Path – Business Card</title>
<link rel="stylesheet" href="https://fonts.googleapis.com/css2?family=Questrial&display=swap">
<style>
  :root {
    --page-bg: #ffffff;
    --card-deep: #0d3a80;
    --card-mid: #12438f;
    --card-light: #1a52a3;
    --text: #ffffff;
    --text-soft: rgba(255, 255, 255, 0.85);
  }
  html, body {
    margin: 0;
    padding: 0;
    width: 1200px;
    height: 900px;
    overflow: hidden;
    background: var(--page-bg);
  }
  .canvas {
    position: relative;
    width: 1200px;
    height: 900px;
    font-family: "Questrial", "Century Gothic", sans-serif;
    color: var(--text);
  }
  .card {
    position: absolute;
    left: 0;
    top: 104px;
    width: 1200px;
    height: 690px;
    border-radius: 28px;
    overflow: hidden;
    background: linear-gradient(165deg, var(--card-light) 0%, var(--card-deep) 50%, var(--card-mid) 100%);
  }
  .brand-name {
    position: absolute;
    left: 56px;
    top: 64px;
    margin: 0;
    font-size: 64px;
    font-weight: 400;
    line-height: 1;
    letter-spacing: 2px;
  }
  .website {
    position: absolute;
    left: 52px;
    top: 175px;
    margin: 0;
    font-size: 26px;
    line-height: 1;
  }
  .tagline {
    position: absolute;
    left: 52px;
    top: 222px;
    margin: 0;
    font-size: 24px;
    line-height: 1;
    color: var(--text-soft);
  }
  .contact-person {
    position: absolute;
    right: 64px;
    top: 258px;
    text-align: right;
  }
  .person-name {
    font-size: 50px;
    line-height: 1;
    margin: 0 0 22px;
  }
  .person-role {
    font-size: 37px;
    line-height: 1;
    margin: 0;
  }
  .details {
    position: absolute;
    left: 54px;
    top: 396px;
    font-size: 39px;
    line-height: 1;
  }
  .address {
    margin: 0;
    font-style: normal;
    line-height: 46px;
  }
  .mobile {
    margin: 26px 0 0;
  }
  .email {
    margin: 30px 0 0;
  }
</style>
</head>
<body>
<div class="canvas">
  <section class="card">
    <h1 class="brand-name">KESTREL PATH</h1>
    <p class="website">www.kestrelpathtrading.com.au</p>
    <p class="tagline">Promotional Merchandise with a difference</p>

    <div class="contact-person">
      <p class="person-name">Peter Hollingdale</p>
      <p class="person-role">Managing Director</p>
    </div>

    <div class="details">
      <address class="address">27 Corbel Street<br>Tarrin Cove 4178</address>
      <p class="mobile">M. 0438 514 203</p>
      <p class="email">kestrelpath@kestrelpathtrading.com.au</p>
    </div>
  </section>
</div>
</body>
</html>
```